Women's Health Company needs business card

We need a business card for a USA based women's health care company. We use digital technology to enhance therapy prescribed by clinicians for their patients

```html
<!DOCTYPE html>
<html lang="en">
<head>
<meta charset="utf-8">
<title>Corvia Health – Stationery</title>
<link href="https://fonts.googleapis.com/css2?family=Lato:wght@400;700&family=Arimo:wght@400&family=Pinyon+Script&display=swap" rel="stylesheet">
<style>
  :root {
    --bg: #e6e6e6;
    --paper: #f4f4f4;
    --purple: #8a4f96;
    --teal: #5fb1ab;
    --teal-light: #7cc9c2;
    --ink: #2b2b2b;
    --muted: #666;
    --rule: #b9b9b9;
  }
  * { margin: 0; padding: 0; box-sizing: border-box; }
  html, body { width: 1200px; height: 942px; overflow: hidden; }
  body {
    position: relative;
    background: var(--bg);
    font-family: 'Lato', sans-serif;
    color: var(--ink);
  }
  .sheet { position: absolute; background: var(--paper); overflow: hidden; }
  .brand-name {
    position: absolute;
    font-family: 'Lato', sans-serif;
    font-weight: 400;
    color: var(--teal);
    white-space: nowrap;
    letter-spacing: 0.02em;
  }
  .base-band { position: absolute; left: 0; right: 0; bottom: 0; background: var(--purple); }

  /* contact blocks */
  .contact { position: absolute; font-family: 'Arimo', sans-serif; color: var(--muted); }
  .contact li { list-style: none; display: flex; align-items: center; white-space: nowrap; }
  .contact svg { fill: var(--purple); flex: none; }
  .address { position: absolute; font-family: 'Arimo', sans-serif; color: var(--muted); white-space: nowrap; }
  .divider { position: absolute; width: 1px; background: var(--teal); }

  /* letterhead */
  .letterhead { left: 157px; top: 151px; width: 436px; height: 616px; }
  .letterhead .brand-name { left: 38px; top: 36px; font-size: 20px; }
  .letterhead .contact { left: 213px; top: 43px; font-size: 7.2px; line-height: 9px; }
  .letterhead .contact svg { width: 5px; height: 5px; margin-right: 6px; }
  .letterhead .divider { left: 308px; top: 44px; height: 25px; }
  .letterhead .address { left: 316px; top: 43px; font-size: 7.2px; line-height: 9px; }
  .letter { position: absolute; left: 46px; top: 180px; width: 343px; font-size: 7px; line-height: 8.8px; }
  .letter .greeting { font-weight: 700; margin-bottom: 8.8px; }
  .letter p { text-align: justify; margin-bottom: 8.8px; }
  .letter .closing { margin-top: 26px; margin-bottom: 6px; }
  .letter .signature { font-family: 'Pinyon Script', cursive; font-size: 13px; line-height: 13px; margin-left: 3px; }
  .letterhead .base-band { height: 7px; }

  /* business card front */
  .card-front { left: 625px; top: 140px; width: 227px; height: 129px; }
  .card-front .brand-name { left: 27px; top: 52px; font-size: 15px; }
  .card-front .divider { left: 114px; top: 32px; height: 64px; }
  .card-front .details { position: absolute; left: 124px; top: 31px; color: var(--muted); font-size: 4.9px; line-height: 6.4px; white-space: nowrap; }
  .card-front .person { color: var(--purple); font-weight: 700; font-size: 6.8px; line-height: 7.5px; }
  .card-front .role { margin-bottom: 6px; }
  .card-front .contact { position: static; margin-top: 6px; font-family: 'Lato', sans-serif; }
  .card-front .contact svg { width: 4px; height: 4px; margin-right: 4px; }
  .card-front .base-band { height: 4px; }

  /* business card back */
  .card-back { left: 897px; top: 140px; width: 227px; height: 129px; background: var(--purple); }
  .card-back .brand-name { right: 26px; top: 79px; font-size: 16px; color: var(--teal-light); }

  /* envelope front */
  .envelope-front { left: 624px; top: 298px; width: 501px; height: 216px; }
  .envelope-front .brand-name { left: 37px; top: 40px; font-size: 24px; }
  .envelope-front .contact { left: 37px; top: 164px; font-size: 7.2px; line-height: 9px; }
  .envelope-front .contact svg { width: 5px; height: 5px; margin-right: 6px; }
  .envelope-front .divider { left: 132px; top: 165px; height: 25px; }
  .envelope-front .address { left: 141px; top: 164px; font-size: 7.2px; line-height: 9px; }
  .envelope-front .base-band { height: 5px; }

  /* envelope back */
  .envelope-back { left: 624px; top: 550px; width: 501px; height: 217px; }
  .envelope-back .flap { position: absolute; left: 0; top: 0; width: 501px; height: 217px; }
  .envelope-back .brand-name { left: 0; right: 0; top: 20px; text-align: center; font-size: 16px; color: var(--teal-light); }
</style>
</head>
<body>

<svg width="0" height="0" style="position:absolute" aria-hidden="true">
  <symbol id="icon-phone" viewBox="0 0 10 10"><path d="M2 0.5 L3.8 0.5 L4.4 2.8 L3.2 3.8 Q4.2 5.9 6.2 6.8 L7.2 5.6 L9.5 6.2 L9.5 8 Q9.5 9.5 8 9.5 Q1 9 0.5 2 Q0.5 0.5 2 0.5Z"/></symbol>
  <symbol id="icon-mail" viewBox="0 0 10 10"><path d="M0.5 2 H9.5 V8 H0.5Z M1 2.5 L5 5.6 L9 2.5" stroke="#f4f4f4" stroke-width="0.8"/></symbol>
  <symbol id="icon-web" viewBox="0 0 10 10"><circle cx="5" cy="5" r="4.5"/><path d="M0.5 5 H9.5 M5 0.5 Q2.5 5 5 9.5 Q7.5 5 5 0.5" fill="none" stroke="#f4f4f4" stroke-width="0.7"/></symbol>
</svg>

<!-- Letterhead -->
<section class="sheet letterhead">
  <div class="brand-name">Corvia Health</div>
  <ul class="contact">
    <li><svg><use href="#icon-phone"/></svg>555.210.7788</li>
    <li><svg><use href="#icon-mail"/></svg>hello@corviahealth.com</li>
    <li><svg><use href="#icon-web"/></svg>www.corviahealth.com</li>
  </ul>
  <div class="divider"></div>
  <div class="address">PO Box 3000<br>Co. Street, Building/Suite<br>City/State, Zip Code</div>

  <div class="letter">
    <div class="greeting">Dear Laura Bennett,</div>
    <p>Lorem ipsum dolor sit amet, consectetuer adipiscing elit, sed diam nonummy nibh euismod tincidunt ut laoreet dolore magna aliquam erat volutpat. Ut wisi enim ad minim veniam, quis nostrud exerci tation ullamcorper suscipit lobortis nisl ut aliquip ex ea commodo consequat. Duis dolore te feugait nulla facilisi. Nam liber tempor cum soluta nobis eleifend option congue nihil imperdiet doming id quod mazim placerat facer possim assum. Lorem ipsum dolor sit amet, consectetuer adipiscing elit, sed diam nonummy nibh euismod tincidunt ut laoreet dolore magna aliquam erat volutpat. Ut wisi enim ad minim veniam, quis nostrud exerci tation ullamcorper suscipit lobortis nisl ut aliquip ex ea commodo consequat.</p>
    <p>Consectetuer adipiscing elit, sed diam nonummy nibh euismod tincidunt ut laoreet dolore magna aliquam erat volutpat. Ut wisi enim ad minim veniam, quis nostrud exerci tation ullamcorper suscipit lobortis nisl ut aliquip ex ea commodo consequat. Consectetuer adipiscing elit, sed diam nonummy nibh euismod tincidunt ut laoreet dolore magna aliquam erat volutpat. Ut wisi enim ad minim veniam, quis nostrud exerci tation ullamcorper suscipit lobortis nisl ut aliquip ex ea commodo consequat.</p>
    <p>Consectetuer adipiscing elit, sed diam nonummy nibh euismod tincidunt ut laoreet dolore magna aliquam erat volutpat. Ut wisi enim ad minim veniam, quis nostrud exerci tation ullamcorper suscipit lobortis nisl ut aliquip ex ea commodo consequat. Consectetuer adipiscing elit, sed diam nonummy nibh euismod tincidunt ut laoreet dolore magna aliquam erat volutpat. Ut wisi enim ad minim veniam, quis nostrud exerci tation ullamcorper suscipit lobortis nisl ut aliquip ex ea commodo consequat.</p>
    <div class="closing">Sincerely Yours</div>
    <div class="signature">Marcus Ellery</div>
    <div>General Manager</div>
  </div>
  <div class="base-band"></div>
</section>

<!-- Business card, front -->
<section class="sheet card-front">
  <div class="brand-name">Corvia Health</div>
  <div class="divider"></div>
  <div class="details">
    <div class="person">Daniel Hartwell</div>
    <div class="role">Managing Director</div>
    <div>PO Box 3000<br>Co. Street, Building/Suite<br>City/State, Zip Code</div>
    <ul class="contact">
      <li><svg><use href="#icon-phone"/></svg>555.210.7788</li>
      <li><svg><use href="#icon-mail"/></svg>hello@corviahealth.com</li>
      <li><svg><use href="#icon-web"/></svg>www.corviahealth.com</li>
    </ul>
  </div>
  <div class="base-band"></div>
</section>

<!-- Business card, back -->
<section class="sheet card-back">
  <div class="brand-name">Corvia Health</div>
</section>

<!-- Envelope, front -->
<section class="sheet envelope-front">
  <div class="brand-name">Corvia Health</div>
  <ul class="contact">
    <li><svg><use href="#icon-phone"/></svg>555.210.7788</li>
    <li><svg><use href="#icon-mail"/></svg>hello@corviahealth.com</li>
    <li><svg><use href="#icon-web"/></svg>www.corviahealth.com</li>
  </ul>
  <div class="divider"></div>
  <div class="address">PO Box 3000<br>Co. Street, Building/Suite<br>City/State, Zip Code</div>
  <div class="base-band"></div>
</section>

<!-- Envelope, back -->
<section class="sheet envelope-back">
  <svg class="flap" viewBox="0 0 501 217" aria-hidden="true">
    <path d="M14 60 L8 70 L8 210 L14 216 M487 60 L493 70 L493 210 L487 216" fill="none" stroke="#cfcfcf" stroke-width="0.8"/>
    <path d="M0 0 H501 L487 62 Q484 71 474 71 H27 Q17 71 14 62 Z" fill="var(--purple)"/>
  </svg>
  <div class="brand-name">Corvia Health</div>
</section>

</body>
</html>
```